Halvern Dental website redesign

We need a redesign for a website: myhalverndental.com.

I already created a video going over what exactly is needed in the design.

See Video here: https://files.quorvane.com/file/d/8xKpQ2mWn4TzLrV7bHsYcE3jFuGaD6oN1/view?usp=sharing

Searchly Slide shown in Video: https://slides.quorvane.com/presentation/d/7RtW2yQnXbVc4LmPz9KsHdJf3GaE8oUi6TeYqNvB5wZx/edit?usp=sharing
Updates

Holidays in India so we did not get enough design entries or quality.

Target Market(s)

Dentistry

Industry/Entity Type

Dentistry

Number of Pages Required

1 page

Colors
0094D4
00A9DD
6FCCEA
C7EBF8
E9F6FB
00AB8E
00BBA5
67D7C9
C6EFE9
E9F9F6

Requirements
Must have
• See 13 min video link in description - shows what to do.

```html
<!DOCTYPE html>
<html lang="en">
<head>
<meta charset="utf-8">
<title>Halvern Dental</title>
<link href="https://fonts.googleapis.com/css2?family=Lato:ital,wght@0,400;0,700;0,900;1,400&display=swap" rel="stylesheet">
<style>
:root{
  --blue:#1e97d6;
  --blue-dark:#1a8bc7;
  --green:#6ab23e;
  --green-logo:#5a9e3a;
  --red:#d0111b;
  --ink:#333;
  --muted:#555;
  --light:#f2f2f2;
  --card:#f4f4f4;
  --icon-bg:#dcf6c9;
  --star:#f7931e;
  --footer:#1f1f1f;
  --line:#d9d9d9;
}
*{box-sizing:border-box;margin:0;padding:0}
html,body{width:1200px;height:4955px;overflow:hidden;background:#fff}
body{font-family:'Lato',sans-serif;color:var(--ink);position:relative}
.abs{position:absolute}
.btn{position:absolute;display:flex;align-items:center;justify-content:center;border-radius:30px;color:#fff;font-weight:900;text-transform:uppercase;text-decoration:none}
.btn-red{background:var(--red)}
.btn-green{background:var(--green)}

/* header */
.brand{position:absolute;left:96px;top:46px;font-size:34px;font-weight:700;color:var(--green-logo);letter-spacing:.5px}
.brand-mark{position:absolute;left:73px;top:54px;width:16px;height:16px;border-radius:50%;background:var(--red)}
.header-city{position:absolute;left:73px;top:125px;font-size:18px;font-weight:700;color:var(--red)}
.header-phone{position:absolute;left:628px;top:68px;font-size:27px;font-weight:700;color:var(--green);display:flex;align-items:center;gap:14px}
.nav{position:absolute;left:0;top:163px;width:1200px;height:64px;background:var(--blue);display:flex;align-items:center;padding-left:102px;gap:0}
.nav a{color:#fff;font-size:14.5px;font-weight:700;text-decoration:none;text-transform:uppercase;margin-right:44px}

/* hero */
.hero{position:absolute;left:0;top:227px;width:1200px;height:667px;background:linear-gradient(100deg,#5a6166 0%,#8a8f93 30%,#c9b6a6 55%,#e6d2c3 75%,#9fb8c4 100%)}
.hero h1{position:absolute;left:73px;top:212px;font-size:51px;line-height:57px;font-weight:900;color:#fff;text-transform:uppercase}
.hero p{position:absolute;left:76px;top:333px;font-size:20px;color:#fff}
.dots{position:absolute;left:552px;top:616px;display:flex;gap:14px}
.dots span{width:16px;height:16px;background:#fff;transform:rotate(45deg)}
.dots span:first-child{background:var(--blue)}

/* welcome */
.welcome-bg{position:absolute;left:0;top:894px}
.welcome-photo{position:absolute;left:73px;top:971px;width:510px;height:389px;border-radius:18px;background:linear-gradient(160deg,#7fb7e6 0%,#cfe6f7 35%,#a25b4a 60%,#6f8a5c 85%,#777 100%)}
.section-title{font-weight:900;text-transform:uppercase}
.welcome h2{position:absolute;left:615px;top:986px;font-size:31px;color:var(--blue)}
.welcome p{position:absolute;left:617px;width:500px;font-size:14.5px;line-height:26px;color:var(--ink)}

/* services */
.services h2{position:absolute;left:0;width:1200px;top:1523px;text-align:center;font-size:32px;color:var(--ink)}
.svc{position:absolute;width:270px;text-align:center}
.svc .ico{width:100px;height:100px;border-radius:50%;background:var(--icon-bg);margin:0 auto}
.svc .lbl{margin-top:34px;font-size:17px;font-weight:700;color:var(--blue);text-transform:uppercase}
.vline{position:absolute;width:1px;background:var(--line)}
.hline{position:absolute;height:2px;background:var(--line)}

/* team */
.team h2{position:absolute;left:0;width:1200px;top:2387px;text-align:center;font-size:32px;color:#fff}
.member{position:absolute;width:300px;text-align:center;color:#fff}
.member .ph{width:250px;height:250px;border-radius:50%;margin:0 auto;background:radial-gradient(circle at 50% 40%,#8a6a58 0%,#4d3a33 55%,#6b6b6b 100%)}
.member .nm{margin-top:26px;font-size:17px;font-weight:700;text-transform:uppercase}
.member .rl{margin-top:6px;font-size:17px;font-weight:700}

/* testimonials */
.reviews h2{position:absolute;left:0;width:1200px;top:3051px;text-align:center;font-size:32px;color:var(--blue)}
.card{position:absolute;top:3129px;width:330px;height:286px;background:var(--card);border-radius:6px;text-align:center}
.card .av{width:100px;height:100px;border-radius:50%;margin:14px auto 0;background:radial-gradient(circle at 50% 40%,#9b6c52,#3a2a25)}
.card .nm{margin-top:28px;font-size:19px;color:var(--ink)}
.stars{color:var(--star);letter-spacing:6px;font-size:20px}
.card .stars{margin-top:4px}
.card .tx{margin:10px auto 0;width:290px;font-size:13.5px;line-height:23px;font-style:italic;color:var(--ink)}
.arrow{position:absolute;top:3250px}
.rating{position:absolute;left:276px;top:3473px;width:200px;text-align:center}
.rating .t{font-size:22px;font-weight:700;text-transform:uppercase}
.rating .s{margin-top:4px;font-size:20px}
.rating .s b{color:var(--ink);font-size:18px;letter-spacing:0}
.rating .r{margin-top:4px;font-size:17px;font-weight:700;color:var(--blue)}
.listing{position:absolute;left:529px;top:3467px;width:394px;height:106px;border:2px solid var(--line);border-radius:4px;display:flex;align-items:center;justify-content:space-around}
.listing span{font-size:26px;font-weight:700;color:var(--ink)}
.listing span.fb{background:#2d4a8a;color:#fff;font-size:19px;padding:9px 10px}

/* experience */
.exp h2{position:absolute;left:73px;top:3711px;font-size:31px;line-height:42px;color:var(--blue)}
.exp p{position:absolute;left:75px;top:3804px;width:510px;font-size:14.5px;line-height:26px;color:var(--muted)}
.exp-photo{position:absolute;left:617px;top:3709px;width:510px;height:389px;border-radius:10px;background:linear-gradient(110deg,#dcdcdc 0%,#f2f2f2 40%,#c9a98f 60%,#e8e8e8 100%)}

/* call to action */
.cta-bg{position:absolute;left:0;top:4210px}
.cta h2{position:absolute;left:0;width:1200px;top:4330px;text-align:center;font-size:34px;color:#fff;font-weight:900;text-transform:uppercase}
.cta p{position:absolute;left:0;width:1200px;top:4384px;text-align:center;font-size:26px;color:#fff}

/* footer */
.footer{position:absolute;left:0;top:4592px;width:1200px;height:363px;background:var(--footer);color:#fff}
.footer .f-brand{position:absolute;left:73px;top:78px;font-size:32px;font-weight:700}
.footer .copy{position:absolute;left:75px;top:172px;font-size:13px;line-height:24px;color:#ccc}
.socials{position:absolute;left:75px;top:245px;display:flex;gap:14px}
.socials span{display:flex;align-items:center;gap:4px;font-size:11px;color:#fff}
.socials i{width:9px;height:9px;border-radius:50%;background:#fff;display:block}
.f-head{position:absolute;font-size:17px;font-weight:900;text-transform:uppercase}
.f-line{position:absolute;font-size:14.5px;color:#eee}
.map{position:absolute;left:656px;top:62px;width:248px;height:231px;background:linear-gradient(135deg,#e9ecef,#d7dde3);border:2px solid #fff}
.hours{position:absolute;left:944px;top:92px;font-size:14.5px;line-height:34px}
.hours td{padding:0;color:#eee}
.hours td:first-child{width:100px}
</style>
</head>
<body>

<!-- header -->
<header>
  <span class="brand-mark"></span>
  <div class="brand">Halvern Dental</div>
  <div class="header-city">Brookfield: (555) 240-7316</div>
  <div class="header-phone">
    <svg width="22" height="24" viewBox="0 0 22 24"><path d="M5 2c1.5 0 2.5 4 2 5.5L5 9c1 3 3 6 6 8l2-2c1.5-.5 5 1 5 2.5l-1 3c-.5 1.5-3 2-5 1C6 19 2 13 2 6c0-2 1.5-4 3-4z" fill="var(--green)"/><path d="M14 4a5 5 0 0 1 4 4M14 0a9 9 0 0 1 8 8" stroke="var(--green)" stroke-width="1.8" fill="none"/></svg>
    (555) 240-7316
  </div>
  <a class="btn btn-red" style="left:885px;top:54px;width:240px;height:61px;font-size:14.5px">Book an Appointment</a>
  <nav class="nav">
    <a>About Us</a><a>Services</a><a>Financing</a><a>Testimonials</a><a>New Patient Visit</a><a>Specials</a><a>Blog</a><a>Contact Us</a>
  </nav>
</header>

<!-- hero -->
<section class="hero" role="img" aria-label="Smiling woman at a dental check-up with a dental mirror">
  <h1>Creating Healthier<br>Smiles</h1>
  <p>With Advanced Technology and Affordable Treatment</p>
  <a class="btn btn-red" style="left:73px;top:390px;width:244px;height:60px;font-size:14.5px">Book an Appointment</a>
  <div class="dots"><span></span><span></span><span></span><span></span></div>
</section>

<!-- welcome -->
<svg class="welcome-bg" width="1200" height="540" viewBox="0 0 1200 540"><path d="M0 0H1200V440C900 440 600 420 300 470C150 495 60 520 0 500Z" fill="var(--light)"/></svg>
<section class="welcome">
  <div class="welcome-photo" role="img" aria-label="Halvern Dental office building exterior"></div>
  <h2 class="section-title">Welcome to Halvern Dental</h2>
  <p style="top:1041px">Your smile is our #1 priority. At Halvern Dental, we provide affordable and expert dental solutions. Whether you are looking for a family dentist or have any emergency such as needing a root canal in Brookfield, we are here for you! We want to keep your teeth healthy inside and out.<br>We don't just clean teeth and send you on your way, we want to get to know you.<br>We accept most HMO and PPO insurances. We offer various financing options through CarePay Plus, LendWell and In-House Plans.</p>
  <a class="btn btn-green" style="left:615px;top:1283px;width:206px;height:50px;font-size:17px">Read More</a>
</section>

<!-- services -->
<section class="services">
  <h2 class="section-title">Our Services</h2>
  <div class="vline" style="left:329px;top:1588px;height:220px"></div>
  <div class="vline" style="left:600px;top:1588px;height:220px"></div>
  <div class="vline" style="left:871px;top:1588px;height:220px"></div>
  <div class="hline" style="left:73px;top:1824px;width:1052px"></div>
  <div class="vline" style="left:329px;top:1846px;height:220px"></div>
  <div class="vline" style="left:600px;top:1846px;height:220px"></div>
  <div class="vline" style="left:871px;top:1846px;height:220px"></div>

  <div class="svc" style="left:52px;top:1621px"><div class="ico" role="img" aria-label="Dental implant icon"></div><div class="lbl">Dental Implants</div></div>
  <div class="svc" style="left:328px;top:1621px"><div class="ico" role="img" aria-label="Cosmetic dentistry icon"></div><div class="lbl">Cosmetic Dentistry</div></div>
  <div class="svc" style="left:602px;top:1621px"><div class="ico" role="img" aria-label="Braces icon"></div><div class="lbl">Braces</div></div>
  <div class="svc" style="left:878px;top:1621px"><div class="ico" role="img" aria-label="Crowns icon"></div><div class="lbl">Crowns</div></div>

  <div class="svc" style="left:52px;top:1883px"><div class="ico" role="img" aria-label="Bridge icon"></div><div class="lbl">Bridge</div></div>
  <div class="svc" style="left:328px;top:1883px"><div class="ico" role="img" aria-label="Extractions icon"></div><div class="lbl">Extractions</div></div>
  <div class="svc" style="left:602px;top:1883px"><div class="ico" role="img" aria-label="Gum disease icon"></div><div class="lbl">Gum Disease</div></div>
  <div class="svc" style="left:878px;top:1883px"><div class="ico" role="img" aria-label="Root canal icon"></div><div class="lbl">Root Canal</div></div>

  <a class="btn btn-green" style="left:498px;top:2127px;width:204px;height:54px;font-size:17px">View All</a>
</section>

<!-- team -->
<svg class="abs" style="left:0;top:2245px" width="1200" height="740" viewBox="0 0 1200 740">
  <defs><linearGradient id="teamGrad" x1="0" y1="0" x2="1" y2="1"><stop offset="0" stop-color="#1e97d6"/><stop offset="0.5" stop-color="#2fa58a"/><stop offset="1" stop-color="#6ab23e"/></linearGradient></defs>
  <path d="M0 100C300 10 700 -20 1200 30V620C900 720 500 760 250 700C150 675 60 650 0 640Z" fill="url(#teamGrad)"/>
</svg>
<section class="team">
  <h2 class="section-title">Meet Our Team</h2>
  <div class="member" style="left:88px;top:2482px"><div class="ph" role="img" aria-label="Portrait of Priya Malhan"></div><div class="nm">Priya Malhan</div><div class="rl">Cosmetic Dentist</div></div>
  <div class="member" style="left:450px;top:2482px"><div class="ph" role="img" aria-label="Portrait of Dr. Reena Kothar"></div><div class="nm">Dr. Reena Kothar</div><div class="rl">Endodontist</div></div>
  <div class="member" style="left:810px;top:2482px"><div class="ph" role="img" aria-label="Portrait of Dr. Vikram Desal"></div><div class="nm">Dr. Vikram Desal</div><div class="rl">General Dentist</div></div>
</section>

<!-- testimonials -->
<section class="reviews">
  <h2 class="section-title">What Our Patients Say About Us</h2>
  <svg class="arrow" style="left:40px" width="20" height="34" viewBox="0 0 20 34"><path d="M17 2L3 17l14 15" stroke="#555" stroke-width="2.5" fill="none"/></svg>
  <svg class="arrow" style="left:1140px" width="20" height="34" viewBox="0 0 20 34"><path d="M3 2l14 15L3 32" stroke="#555" stroke-width="2.5" fill="none"/></svg>

  <div class="card" style="left:73px"><div class="av" role="img" aria-label="Patient photo"></div><div class="nm">Marla D.</div><div class="stars">★★★★★</div><div class="tx">I am so happy I found Halvern Dental in Brookfield. This is a long over due review since I have been seeing them for almost two years.</div></div>
  <div class="card" style="left:436px"><div class="av" role="img" aria-label="Patient photo"></div><div class="nm">Marla D.</div><div class="stars">★★★★★</div><div class="tx">I am so happy I found Halvern Dental in Brookfield. This is a long over due review since I have been seeing them for almost two years.</div></div>
  <div class="card" style="left:796px"><div class="av" role="img" aria-label="Patient photo"></div><div class="nm">Marla D.</div><div class="stars">★★★★★</div><div class="tx">I am so happy I found Halvern Dental in Brookfield. This is a long over due review since I have been seeing them for almost two years.</div></div>

  <div class="rating">
    <div class="t">Average Rating</div>
    <div class="s stars">★★★★★<b>4.2</b></div>
    <div class="r">237 Reviews</div>
  </div>
  <div class="listing"><span>Reviewly</span><span>Searchly</span><span class="fb">Friendbook</span></div>
  <div class="hline" style="left:73px;top:3634px;width:1052px;height:1px"></div>
</section>

<!-- experience -->
<section class="exp">
  <h2 class="section-title">Experience the Halvern<br>Dental Difference</h2>
  <p>Sed ut perspiciatis unde omnis iste natus error sit voluptatem accusantium doloremque laudantium, totam rem aperiam, eaque ipsa quae ab illo inventore veritatis et quasi architecto beatae vitae dicta sunt explicabo. Nemo enim ipsam voluptatem quia voluptas sit aspernatur aut odit aut fugit, sed quia consequuntur magni dolores eos qui ratione voluptatem sequi nesciunt. Neque porro quisquam est, qui dolorem ipsum quia dolor sit amet, consectetur, adipisci velit, sed quia non numquam eius modi tempora incidunt ut labore et dolore .</p>
  <a class="btn btn-green" style="left:73px;top:4042px;width:206px;height:54px;font-size:17px">Read More</a>
  <div class="exp-photo" role="img" aria-label="Dentist in white coat with a smiling patient in the dental chair"></div>
</section>

<!-- call to action -->
<svg class="cta-bg" width="1200" height="385" viewBox="0 0 1200 385" role="img" aria-label="Dark modern dental treatment room">
  <defs><linearGradient id="ctaGrad" x1="0" y1="0" x2="1" y2="1"><stop offset="0" stop-color="#0d2c3a"/><stop offset="0.5" stop-color="#164a5a"/><stop offset="1" stop-color="#0a2230"/></linearGradient></defs>
  <path d="M0 40C300 70 700 80 900 40C1000 20 1100 5 1200 0V385H0Z" fill="url(#ctaGrad)"/>
</svg>
<section class="cta">
  <h2>Committed to Excellence in Oral Health Care</h2>
  <p>Free Exam and X-Rays for New Patients</p>
  <a class="btn btn-green" style="left:427px;top:4450px;width:346px;height:58px;font-size:17px">Book an Appointment</a>
</section>

<!-- footer -->
<footer class="footer">
  <div class="f-brand">Halvern Dental</div>
  <div class="copy">Copyright ©2021 Company Name.<br>All Rights Reserved.</div>
  <div class="socials"><span><i></i>Sharely</span><span><i></i>Chirpr</span><span><i></i>Snapgram</span><span><i></i>Workedin</span><span><i></i>Vidtube</span></div>

  <div class="f-head" style="left:342px;top:58px">Contact Us</div>
  <div class="f-line" style="left:342px;top:96px">482 West Alder Ave., Suite A</div>
  <div class="f-line" style="left:342px;top:125px">Brookfield, CA 90417</div>
  <div class="f-line" style="left:342px;top:161px">(555) 240-7316</div>
  <div class="f-line" style="left:342px;top:190px">hello@myhalverndental.com</div>
  <a class="btn btn-green" style="left:342px;top:240px;width:293px;height:54px;font-size:17px;text-transform:none;font-weight:700">Book Your Free Consultation</a>

  <div class="map" role="img" aria-label="Street map showing the Halvern Dental location"></div>

  <div class="f-head" style="left:944px;top:58px">Hours</div>
  <table class="hours">
    <tr><td>Monday</td><td>10AM–7PM</td></tr>
    <tr><td>Tuesday</td><td>10AM–7PM</td></tr>
    <tr><td>Wednesday</td><td>9AM–6PM</td></tr>
    <tr><td>Thursday</td><td>9AM–6PM</td></tr>
    <tr><td>Friday</td><td>9AM–5PM</td></tr>
    <tr><td>Saturday</td><td>9AM–1PM</td></tr>
  </table>
</footer>

</body>
</html>
```